need a clean, modern job advertisement designed for social media (Facebook & Instagram).

The post is to advertise two positions:
• Leading Hand Boilermaker
• Dragline Fitter
We want the design to match our KRT Plant Services branding: blue, white, strong, professional, mining-industry style.
What the design should include:
Bold headline: “WE’RE HIRING”
Sub-headline: “Leading Hand Boilermaker & Dragline Fitter”
Key points:
• Bowen Basin based
• Dragline & shovel maintenance
• Great pay + long-term work
• Locally owned & operated
KRT logo placed cleanly
Space for 1–2 images (boilermaking or dragline work)
Design style:
Strong and industrial
Blue/white colour scheme
Easy to read at a glance
Suitable for a square 1080×1080 design

```html
<!DOCTYPE html>
<html lang="en">
<head>
<meta charset="utf-8">
<title>KRT Plant Services – We're Hiring</title>
<link rel="stylesheet" href="https://fonts.googleapis.com/css2?family=Bebas+Neue&family=Roboto+Condensed:wght@400;500&display=swap">
<style>
  :root {
    --ink: #000000;
    --paper: #ffffff;
    --brand-blue: #00aaf5;
    --photo-deep: #0c1a33;
    --photo-mid: #1f4a7a;
    --spark: #d9782a;
  }
  html, body {
    margin: 0;
    width: 1200px;
    height: 1200px;
    overflow: hidden;
    background: var(--paper);
  }
  .post {
    position: relative;
    width: 1080px;
    height: 1080px;
    transform: scale(1.111111);
    transform-origin: 0 0;
    background: var(--ink);
  }
  .post__shapes {
    position: absolute;
    inset: 0;
    width: 1080px;
    height: 1080px;
  }
  .brand {
    position: absolute;
    left: 640px;
    top: 70px;
    width: 330px;
    text-align: center;
    font-family: "Bebas Neue", sans-serif;
    color: var(--ink);
    line-height: 0.9;
  }
  .brand__name { font-size: 120px; display: block; letter-spacing: 4px; }
  .brand__tag { font-size: 44px; display: block; letter-spacing: 2px; }
  .headline {
    position: absolute;
    left: 604px;
    top: 318px;
    margin: 0;
    font-family: "Bebas Neue", sans-serif;
    font-weight: 400;
    font-size: 166px;
    line-height: 0.78;
    letter-spacing: 2px;
  }
  .headline__lead { color: var(--brand-blue); display: block; }
  .headline__main { color: var(--ink); display: block; margin-top: 18px; }
  .roles {
    position: absolute;
    left: 605px;
    top: 628px;
    margin: 0;
    font-family: "Bebas Neue", sans-serif;
    font-weight: 400;
    font-size: 74px;
    line-height: 0.93;
    color: var(--paper);
    letter-spacing: 1px;
  }
  .highlights {
    position: absolute;
    left: 604px;
    top: 868px;
    margin: 0;
    padding: 0;
    list-style: none;
    font-family: "Roboto Condensed", sans-serif;
    font-size: 28px;
    line-height: 44.5px;
    color: var(--ink);
  }
  .highlights li::before { content: "•"; margin-right: 10px; }
</style>
</head>
<body>
<main class="post">
  <svg class="post__shapes" viewBox="0 0 1080 1080" aria-hidden="false">
    <defs>
      <radialGradient id="weld-glow" cx="0.35" cy="0.7" r="0.8">
        <stop offset="0" stop-color="var(--spark)"/>
        <stop offset="0.35" stop-color="#5a3a2a"/>
        <stop offset="0.7" stop-color="var(--photo-mid)"/>
        <stop offset="1" stop-color="var(--photo-deep)"/>
      </radialGradient>
    </defs>
    <rect class="panel-white" x="14" y="14" width="1052" height="1052" fill="var(--paper)"/>
    <polygon class="photo-welder" role="img" aria-label="Photo of a welder in a blue helmet with sparks flying"
      points="14,14 505,14 545,210 245,1066 14,1066" fill="url(#weld-glow)"/>
    <polygon class="chevron-black" points="505,14 578,14 602,210 505,540 305,1066 245,1066 545,210" fill="var(--ink)"/>
    <polygon class="chevron-blue-top" points="578,14 612,14 596,118" fill="var(--brand-blue)"/>
    <polygon class="chevron-blue-low" points="450,480 508,548 308,1066 245,1066" fill="var(--brand-blue)"/>
    <polygon class="roles-band" points="542,607 1066,607 1066,853 474,853" fill="var(--ink)"/>
  </svg>

  <div class="brand">
    <span class="brand__name">KRT</span>
    <span class="brand__tag">Plant Services</span>
  </div>

  <h1 class="headline">
    <span class="headline__lead">We’re</span>
    <span class="headline__main">Hiring</span>
  </h1>

  <h2 class="roles">Leading Hand<br>Boilermaker &amp;<br>Dragline Fitter</h2>

  <ul class="highlights">
    <li>Bowen Basin based</li>
    <li>Dragline &amp; shovel maintenance</li>
    <li>Great pay + long-term work</li>
    <li>Locally owned &amp; operated</li>
  </ul>
</main>
</body>
</html>
```